CEO Business card - hotels and restaurant

Business card for the General Manager of 3 different businesses: 2 hotels and 1 restaurant:
Casa Ribeira Hotel
Monte Sereno - Lagos Hotel
pão com toda alegria sempre restaurant
Name and contact details:
Rui Fontoura Braga
CEO
E-mail: rui.braga@hotelcasaribeira.com
Mobile: +351 916 447 215
Please find the attached logos. You may also google it for the 3 businesses

Industry/Entity Type

Hospitality

Contact Information for Business Card

Rui Fontoura Braga
CEO

Font styles to use
Script

Colors

Designer to choose colors to be used in the design.

Requirements
Must have
• Front - Name, position and contact details
• Back - Businesses logos and info of each one
• HOTEL CASA RIBEIRA
• Address: Rua das Acácias - Nº 173 | 2440-999 BATALHA - PORTUGAL
• Phone: +351 244 551 930
• E-mail: geral@hotelcasaribeira.pt
• HOTEL MONTE SERENO - LAGOS
• Address: Avenida das Tílias, s/n | 7350-999 ELVAS - PORTUGAL
• Phone: +351 268 812 364
• E-mail: geral@hotelmsereno-lagos.pt
• "pão com toda alegria sempre" RESTAURANT
• Address: Estrada do Moinho, 42 | 2440-999 BATALHA - PORTUGAL
• Phone: +351 244 593 218
• E-mail: info@pctas.pt
Nice to have
• Something elegant and stylish but professional and very wow effect

```html
<!DOCTYPE html>
<html lang="pt">
<head>
<meta charset="utf-8">
<title>Rui Fontoura Braga – Business Card</title>
<link rel="stylesheet" href="https://fonts.googleapis.com/css2?family=Cinzel:wght@400&family=Open+Sans:wght@400;700&display=swap">
<style>
  :root {
    --backdrop: #d1d2d4;
    --ink-black: #151515;
    --paper: #ffffff;
    --wine: #8c1c48;
    --text-dark: #1d1d1d;
    --text-grey: #555555;
    --divider: #6b6b6b;
  }
  * { margin: 0; padding: 0; box-sizing: border-box; }
  html, body { width: 1200px; height: 1000px; overflow: hidden; background: var(--backdrop); }
  body { position: relative; font-family: "Open Sans", sans-serif; }

  .card { position: absolute; left: 242px; width: 716px; height: 419px; overflow: hidden; }
  .card--front { top: 64px; background: var(--ink-black); }
  .card--back { top: 517px; background: var(--paper); }

  .front-shape { position: absolute; inset: 0; }

  .holder-name {
    position: absolute; top: 62px; left: 0; width: 100%;
    text-align: center; font-family: "Cinzel", serif; font-size: 40px;
    color: #f2f2f2; letter-spacing: 1px; line-height: 1;
  }
  .holder-role {
    position: absolute; top: 113px; left: 0; width: 100%;
    text-align: center; font-family: "Cinzel", serif; font-size: 30px;
    color: #f2f2f2; letter-spacing: 16px; padding-left: 16px; line-height: 1;
  }

  .front-contact { position: absolute; left: 0; width: 100%; text-align: center; }
  .front-contact .badge { display: block; margin: 0 auto; width: 32px; height: 32px; }
  .front-contact .value { display: block; margin-top: 8px; font-size: 17px; color: var(--text-dark); }
  .front-contact--phone { top: 213px; }
  .front-contact--mail { top: 306px; }

  .venue { position: absolute; left: 0; width: 100%; height: 98px; }
  .venue--one { top: 39px; }
  .venue--two { top: 163px; }
  .venue--three { top: 287px; }

  .venue-mark {
    position: absolute; left: 30px; top: 0; width: 176px; height: 98px;
    display: flex; align-items: center; justify-content: center; gap: 8px;
    font-size: 19px; font-weight: 700; color: var(--wine); text-align: center; line-height: 1.15;
  }
  .venue-mark .dot { width: 14px; height: 14px; border-radius: 50%; background: var(--wine); flex: none; }
  .venue-divider { position: absolute; left: 204px; top: 0; width: 1.5px; height: 98px; background: var(--divider); }

  .venue-info { position: absolute; left: 226px; top: 4px; }
  .venue-title { font-size: 16px; font-weight: 700; color: var(--text-dark); line-height: 20px; margin-bottom: 1px; }
  .venue-line { display: flex; align-items: center; font-size: 14.5px; color: var(--text-grey); line-height: 20px; }
  .venue-line svg { width: 17px; height: 17px; margin-right: 4px; flex: none; }
</style>
</head>
<body>

<svg width="0" height="0" style="position:absolute" aria-hidden="true">
  <defs>
    <symbol id="icon-phone" viewBox="0 0 32 32">
      <circle cx="16" cy="16" r="16" fill="#8c1c48"/>
      <path d="M21.5 7.5l2.5 2.5-2.6 2.6-1.6-1.1-6 6 1.1 1.6-2.6 2.6-2.5-2.5c-.6-.6-.6-1.6 0-2.2l9.5-9.5c.6-.6 1.6-.6 2.2 0z" fill="#fff" transform="rotate(180 16 16) translate(0 0)"/>
    </symbol>
    <symbol id="icon-mail" viewBox="0 0 32 32">
      <circle cx="16" cy="16" r="16" fill="#8c1c48"/>
      <rect x="8.5" y="10.5" width="15" height="11" rx="1" fill="#fff"/>
      <path d="M8.8 11l7.2 6 7.2-6" fill="none" stroke="#8c1c48" stroke-width="1.6"/>
    </symbol>
    <symbol id="icon-pin" viewBox="0 0 32 32">
      <circle cx="16" cy="16" r="16" fill="#8c1c48"/>
      <path d="M16 7a6 6 0 0 0-6 6c0 4.5 6 12 6 12s6-7.5 6-12a6 6 0 0 0-6-6z" fill="#fff"/>
      <circle cx="16" cy="13" r="2.3" fill="#8c1c48"/>
    </symbol>
  </defs>
</svg>

<section class="card card--front" aria-label="Card front">
  <svg class="front-shape" viewBox="0 0 716 419" aria-hidden="true">
    <polygon points="282,130 435,130 716,419 0,419" fill="#ffffff"/>
    <line x1="0" y1="129" x2="716" y2="129" stroke="#8c1c48" stroke-width="2"/>
    <rect x="282" y="128" width="153" height="34" fill="#151515"/>
    <polyline points="282,129 282,161 435,161 435,129" fill="none" stroke="#8c1c48" stroke-width="2"/>
  </svg>
  <h1 class="holder-name">Rui Fontoura Braga</h1>
  <p class="holder-role">CEO</p>

  <div class="front-contact front-contact--phone">
    <svg class="badge"><use href="#icon-phone"/></svg>
    <span class="value">+351 916 447 215</span>
  </div>
  <div class="front-contact front-contact--mail">
    <svg class="badge"><use href="#icon-mail"/></svg>
    <span class="value">rui.braga@hotelcasaribeira.com</span>
  </div>
</section>

<section class="card card--back" aria-label="Card back">
  <article class="venue venue--one">
    <div class="venue-mark"><span class="dot"></span><span>Casa Ribeira</span></div>
    <div class="venue-divider"></div>
    <div class="venue-info">
      <h2 class="venue-title">HOTEL CASA RIBEIRA</h2>
      <p class="venue-line"><svg><use href="#icon-pin"/></svg>Rua das Acácias - Nº 173 | 2440-999 BATALHA - PORTUGAL</p>
      <p class="venue-line"><svg><use href="#icon-phone"/></svg>+351 244 551 930</p>
      <p class="venue-line"><svg><use href="#icon-mail"/></svg>geral@hotelcasaribeira.pt</p>
    </div>
  </article>

  <article class="venue venue--two">
    <div class="venue-mark"><span class="dot"></span><span>Monte Sereno</span></div>
    <div class="venue-divider"></div>
    <div class="venue-info">
      <h2 class="venue-title">HOTEL MONTE SERENO - LAGOS</h2>
      <p class="venue-line"><svg><use href="#icon-pin"/></svg>Rua das Acácias - Nº 173 | 2440-999 BATALHA - PORTUGAL</p>
      <p class="venue-line"><svg><use href="#icon-phone"/></svg>+351 268 812 364</p>
      <p class="venue-line"><svg><use href="#icon-mail"/></svg>geral@hotelmsereno-lagos.pt</p>
    </div>
  </article>

  <article class="venue venue--three">
    <div class="venue-mark"><span class="dot"></span><span>pão com toda<br>alegria sempre</span></div>
    <div class="venue-divider"></div>
    <div class="venue-info">
      <h2 class="venue-title">RESTAURANT "pão com toda alegria sempre"</h2>
      <p class="venue-line"><svg><use href="#icon-pin"/></svg>Estrada do Moinho, 42 | 2440-999 BATALHA - PORTUGAL</p>
      <p class="venue-line"><svg><use href="#icon-phone"/></svg>+351 244 593 218</p>
      <p class="venue-line"><svg><use href="#icon-mail"/></svg>info@pctas.pt</p>
    </div>
  </article>
</section>

</body>
</html>
```